Engineering Consultant Business Card

I'm starting a new business as a high-end engineering consultant in a niche field. I've attached the jpg for my logo plus the branding guideline document that I've been following. You can see my business website here: www.tarvikworks.com
I'd like a business card that has the logo on one side, then the other side has (in any order): Tarvik Works, Inc.
Dana Whitlock
President and Chief EMC Engineer
www.tarvikworks.com
dana@tarvikworks.com
Optional: motto "We will solve your EMC problems as early as possible—ideally before they even start."
I'm not planning on including a phone number
Target Market(s)
Businesses, especially makers of electronics hardware
Industry/Entity Type
Electrical engineering
Contact Information for Business Card
Company name, my name, website, email

```html
<!DOCTYPE html>
<html lang="en">
<head>
<meta charset="utf-8">
<title>Tarvik Works, Inc. — Business Card</title>
<link rel="stylesheet" href="https://fonts.googleapis.com/css2?family=Montserrat:ital,wght@0,400;0,500;0,600;1,500&display=swap">
<style>
  :root {
    --brand-blue: #2c459e;
    --paper: #ffffff;
    --ink: #111111;
    --backdrop: #95999c;
  }
  * { margin: 0; padding: 0; box-sizing: border-box; }
  html, body {
    width: 1200px;
    height: 1200px;
    overflow: hidden;
    background: var(--backdrop);
    font-family: "Montserrat", Arial, sans-serif;
  }
  .card {
    position: absolute;
    left: 291px;
    width: 619px;
    height: 400px;
    overflow: hidden;
  }
  .card--front {
    top: 176px;
    background: var(--brand-blue);
    display: flex;
    align-items: center;
    justify-content: center;
    gap: 16px;
  }
  .wordmark {
    display: flex;
    align-items: center;
    gap: 12px;
    font-weight: 600;
  }
  .wordmark__dot {
    border-radius: 50%;
    flex: none;
  }
  .card--front .wordmark { color: var(--paper); font-size: 44px; }
  .card--front .wordmark__dot { width: 34px; height: 34px; background: var(--paper); }

  .card--back {
    top: 649px;
    background: var(--paper);
  }
  .card--back .wordmark {
    position: absolute;
    left: 37px;
    top: 52px;
    color: var(--brand-blue);
    font-size: 20px;
    gap: 8px;
  }
  .card--back .wordmark__dot { width: 18px; height: 18px; background: var(--brand-blue); }

  .company {
    position: absolute;
    right: 41px;
    top: 47px;
    font-size: 21px;
    font-weight: 500;
    color: var(--ink);
  }
  .person__name {
    position: absolute;
    left: 38px;
    top: 118px;
    font-size: 21px;
    font-weight: 600;
    color: var(--brand-blue);
  }
  .person__title {
    position: absolute;
    left: 38px;
    top: 148px;
    font-size: 15.5px;
    font-weight: 400;
    color: var(--ink);
  }
  .contact__label {
    position: absolute;
    left: 38px;
    display: flex;
    align-items: center;
    gap: 11px;
  }
  .contact__rule {
    width: 53px;
    height: 2px;
    background: var(--brand-blue);
  }
  .contact__value {
    position: absolute;
    left: 38px;
    font-size: 15.5px;
    font-weight: 400;
    color: var(--ink);
  }
  .contact--email .contact__label { top: 177px; }
  .contact--email .contact__value { top: 201px; }
  .contact--web .contact__label { top: 232px; }
  .contact--web .contact__value { top: 257px; }

  .motto-band {
    position: absolute;
    left: 0;
    bottom: 0;
    width: 100%;
    height: 89px;
    background: var(--brand-blue);
    display: flex;
    align-items: center;
    justify-content: center;
  }
  .motto {
    color: var(--paper);
    font-style: italic;
    font-weight: 500;
    font-size: 15px;
    line-height: 23px;
    text-align: center;
  }
</style>
</head>
<body>
  <section class="card card--front" aria-label="Card front">
    <div class="wordmark"><span class="wordmark__dot"></span>Tarvik Works</div>
  </section>

  <section class="card card--back" aria-label="Card back">
    <div class="wordmark"><span class="wordmark__dot"></span>Tarvik Works</div>
    <p class="company">Tarvik Works, Inc.</p>

    <h1 class="person__name">Dana Whitlock</h1>
    <p class="person__title">(President and Chief EMC Engineer)</p>

    <div class="contact contact--email">
      <div class="contact__label">
        <svg width="20" height="14" viewBox="0 0 20 14" aria-hidden="true">
          <rect x="0.75" y="0.75" width="18.5" height="12.5" fill="var(--brand-blue)"/>
          <path d="M1 1 L10 8 L19 1 M1 13 L7.5 6.5 M19 13 L12.5 6.5" fill="none" stroke="#fff" stroke-width="1.2"/>
        </svg>
        <span class="contact__rule"></span>
      </div>
      <p class="contact__value">dana@tarvikworks.com</p>
    </div>

    <div class="contact contact--web">
      <div class="contact__label">
        <svg width="20" height="20" viewBox="0 0 20 20" aria-hidden="true">
          <g fill="none" stroke="var(--brand-blue)" stroke-width="1.6">
            <circle cx="9" cy="9" r="7.5"/>
            <ellipse cx="9" cy="9" rx="3.2" ry="7.5"/>
            <path d="M1.5 9 H16.5 M2.8 5 H15.2 M2.8 13 H15.2"/>
          </g>
          <path d="M11 10 L11 19 L13.2 16.8 L15 20 L16.3 19.3 L14.6 16.2 L17.5 16 Z" fill="var(--brand-blue)" stroke="#fff" stroke-width="0.8"/>
        </svg>
        <span class="contact__rule"></span>
      </div>
      <p class="contact__value">www.tarvikworks.com</p>
    </div>

    <div class="motto-band">
      <p class="motto">We will solve your EMC problems as early as possible -<br>ideally before they even start</p>
    </div>
  </section>
</body>
</html>
```